Retro game shop business card design

We need a card designed both front and back. we already have a logo. The business name is called Brisk Copper Atlas and we work on customizing and modifying old velmora zuma tabs. Our website is briskcopperatlas.com

our business cards are often shown in glintly posts ans should be designed so that you can easy identify and see in am image. @briskcopperatlas.

Target Market(s)

men 13-40

Contact Information for Business Card

should have logo, wesbite, and if possible some artwork related to zuma tab mods

Font styles to use
Sans Serif

Colors

Designer to choose colors to be used in the design.

Requirements
Must have
• logo, website url www.briskcopperatlas.com, hastag #zumatabmods, email, support@briskcopperatlas.com. zuma tab imagry only (illustration preffered)
Nice to have
• illustrations, graphic design with zuma tab mods (see glintly #zumatabmods)
Should not have
• childlike depictions of zumatabs, kids, anything unrelated to zuma tab mods, no hands, no bertil, no pixel art

```html
<!DOCTYPE html>
<html lang="en">
<head>
<meta charset="utf-8">
<title>Brisk Copper Atlas — Business Card</title>
<link href="https://fonts.googleapis.com/css2?family=Open+Sans:wght@400;600;700;800&display=swap" rel="stylesheet">
<style>
  :root {
    --backdrop: #e6e7e8;
    --panel: #ffffff;
    --ink: #000000;
    --muted: #8a8a8a;
    --rule: #8f8f8f;
    --paper: #ffffff;
  }
  * { margin: 0; padding: 0; box-sizing: border-box; }
  html, body { width: 1200px; height: 1200px; overflow: hidden; }
  body {
    background: var(--backdrop);
    font-family: "Open Sans", sans-serif;
    color: var(--ink);
    position: relative;
  }
  .sheet {
    position: absolute;
    left: 255px;
    width: 731px;
    height: 482px;
    background: var(--panel);
    border-radius: 8px;
  }
  .sheet--front { top: 69px; }
  .sheet--back { top: 598px; }

  /* Front card */
  .card-front {
    position: absolute;
    left: 36px; top: 24px;
    width: 659px; height: 434px;
    border: 1px solid var(--ink);
    border-radius: 8px;
  }
  .wordmark {
    font-weight: 800;
    text-transform: uppercase;
    line-height: 1;
    letter-spacing: 0.5px;
  }
  .card-front .wordmark {
    position: absolute;
    left: 22px; top: 157px;
    font-size: 32px;
    color: var(--ink);
  }
  .card-front .wordmark span { display: block; }
  .card-front .wordmark span + span { margin-top: 6px; }
  .divider {
    position: absolute;
    left: 312px; top: 148px;
    width: 3px; height: 134px;
    background: var(--rule);
  }
  .person {
    position: absolute;
    left: 350px; top: 150px;
  }
  .person-name { font-size: 32px; font-weight: 600; line-height: 1; }
  .person-role { font-size: 15px; font-weight: 600; color: var(--muted); margin-top: 2px; }
  .contact-list {
    position: absolute;
    left: 350px; top: 222px;
    list-style: none;
  }
  .contact-list li {
    display: flex; align-items: center; gap: 12px;
    font-size: 15.5px; font-weight: 600;
    height: 24px;
  }
  .contact-list li + li { margin-top: 7px; }
  .contact-list svg { width: 22px; height: 22px; flex: none; }
  .address {
    position: absolute;
    left: 0; right: 0; top: 368px;
    display: flex; justify-content: center; align-items: center; gap: 10px;
    font-size: 21px;
  }
  .address svg { width: 20px; height: 24px; }

  /* Back card */
  .card-back {
    position: absolute;
    left: 29px; top: 25px;
    width: 674px; height: 433px;
  }
  .card-back-shape { position: absolute; inset: 0; }
  .card-back .wordmark {
    position: absolute;
    left: 0; right: 0; top: 130px;
    text-align: center;
    font-size: 64px;
    color: var(--paper);
  }
  .card-back .wordmark span { display: block; }
  .card-back .wordmark span + span { margin-top: 8px; }
  .social-row {
    position: absolute;
    left: 0; right: 0; top: 328px;
    display: flex; justify-content: center; align-items: center; gap: 8px;
  }
  .social-row .rule { width: 74px; height: 2px; background: var(--paper); }
  .social-row .dot {
    width: 34px; height: 34px;
    border: 2px solid var(--paper);
    border-radius: 50%;
  }
  .handle {
    position: absolute;
    left: 0; right: 0; top: 372px;
    text-align: center;
    color: var(--paper);
    font-size: 18px;
  }
</style>
</head>
<body>

<section class="sheet sheet--front">
  <div class="card-front">
    <div class="wordmark"><span>Brisk Copper</span><span>Atlas</span></div>
    <div class="divider"></div>
    <div class="person">
      <p class="person-name">Dorian</p>
      <p class="person-role">CEO</p>
    </div>
    <ul class="contact-list">
      <li>
        <svg viewBox="0 0 24 24" fill="none" stroke="#000" stroke-width="1.4"><rect x="2" y="5" width="20" height="14"/><path d="M2 5l10 8 10-8M2 19l7-7M22 19l-7-7"/></svg>
        support@briskcopperatlas.com
      </li>
      <li>
        <svg viewBox="0 0 24 24" fill="none" stroke="#000" stroke-width="1.3"><circle cx="12" cy="12" r="10"/><ellipse cx="12" cy="12" rx="4.5" ry="10"/><path d="M2 12h20M4 6.5h16M4 17.5h16"/></svg>
        www.briskcopperatlas.com
      </li>
    </ul>
    <p class="address">
      <svg viewBox="0 0 20 24" fill="none" stroke="#000" stroke-width="1.5"><path d="M10 23s-8-8.5-8-14a8 8 0 0 1 16 0c0 5.5-8 14-8 14z"/><circle cx="10" cy="9" r="3"/></svg>
      57 Harrow Lane, Fenwick Hollow, PA 19088
    </p>
  </div>
</section>

<section class="sheet sheet--back">
  <div class="card-back">
    <svg class="card-back-shape" viewBox="0 0 674 433" aria-hidden="true">
      <path d="M24 0H650a24 24 0 0 1 24 24V288C674 378 650 433 560 433H24A24 24 0 0 1 0 409V24A24 24 0 0 1 24 0z" fill="var(--ink)"/>
    </svg>
    <div class="wordmark"><span>Brisk Copper</span><span>Atlas</span></div>
    <div class="social-row">
      <span class="rule"></span>
      <span class="dot"></span>
      <span class="dot"></span>
      <span class="dot"></span>
      <span class="rule"></span>
    </div>
    <p class="handle">@briskcopperatlas</p>
  </div>
</section>

</body>
</html>
```